Large Financial Advisory Firm Needs a Brochure!

We are looking for a modern and professional 4 page brochure for our Financial Advisory firm, Harbrook Counsel Group. I've attached multiple files to help with the completion of the design.
SIZE OF BROCHURE: 17 x 11 FLAT, 8.5 x 11 inch FOLDED
1. A PDF titled Design Brief will provide you with an overview of the project, the text to be included in the brochure and other misc. instructions.
2. Logo Files, you will need to incorporate our logo into the brochure design, I've attached all the files please select the images that suit your design.
3. Competitor Illustration - I've attached an image that needs to be included on the 2nd page (inside left cover of the brochure). You will need to incorporate the pros/cons of using our competitors and the advantages of using our firm. This is outlined in the Design Brief PDF.
NOTE: If possible please get rid of the blue sky in the illustration. Just use the buildings, the blue throws off the concept. I contacted the illustrator and am waiting for a design without the sky but it may not be ready in time so please delete it if possible.
- I like the Avenir fonts, 85 Heavy, 65 Medium and 45.

```html
<!DOCTYPE html>
<html lang="en">
<head>
<meta charset="utf-8">
<title>Harbrook Counsel Group – Brochure Spread</title>
<link rel="stylesheet" href="https://fonts.googleapis.com/css2?family=Mulish:wght@300;400;700;900&display=swap">
<style>
  :root {
    --gold: #f2b52c;
    --gold-deep: #e9a51c;
    --gold-soft: #f8d788;
    --ink: #1a1a1a;
    --body-text: #3c3c3c;
    --paper: #ffffff;
    --paper-shade: #f1f1f1;
    --backdrop: #4a4a4a;
    --rule: #f0cf82;
  }
  * { margin: 0; padding: 0; box-sizing: border-box; }
  html, body { width: 1200px; height: 954px; overflow: hidden; }
  body {
    background: var(--backdrop);
    font-family: "Mulish", sans-serif;
    position: relative;
  }
  .spread {
    position: absolute;
    left: 60px; top: 110px;
    width: 1080px; height: 734px;
    display: flex;
  }
  .page { position: relative; width: 540px; height: 734px; overflow: hidden; }

  /* Inside page */
  .team-page { background: linear-gradient(90deg, var(--paper) 88%, var(--paper-shade)); }
  .team-sidebar {
    position: absolute; left: 20px; top: 25px;
    width: 122px; height: 525px;
    background: var(--gold);
  }
  .team-heading {
    position: absolute; left: 14px; top: 20px;
    color: var(--paper); font-weight: 400; font-size: 17px; letter-spacing: 0.4px;
    white-space: nowrap;
  }
  .member-card { position: absolute; left: 15px; width: 104px; }
  .member-card:nth-of-type(1) { top: 58px; }
  .member-card:nth-of-type(2) { top: 223px; }
  .member-card:nth-of-type(3) { top: 387px; }
  .member-photo {
    width: 90px; height: 92px;
    background: linear-gradient(160deg, #b48a55, #5a4330 55%, #1f2430);
  }
  .member-name {
    color: var(--paper); font-weight: 700; font-size: 10.5px; margin-top: 7px;
    line-height: 1.15; white-space: nowrap;
  }
  .member-title { color: var(--paper); font-weight: 300; font-size: 9.5px; line-height: 1.2; }

  .bio {
    position: absolute; left: 147px; width: 356px;
    font-size: 7.5px; line-height: 10.3px; color: var(--body-text);
  }
  .bio p + p { margin-top: 4px; }
  .bio.first { top: 70px; }
  .bio.second { top: 245px; }
  .bio.third { top: 412px; }
  .bio-rule {
    position: absolute; left: 147px; width: 356px;
    border: 0; border-top: 1px solid var(--rule);
  }
  .bio-rule.first { top: 225px; }
  .bio-rule.second { top: 395px; }

  .wordmark {
    position: absolute; display: flex; flex-direction: column; align-items: center;
    color: var(--ink); font-weight: 900; text-align: center;
  }
  .wordmark-square { width: 68px; height: 68px; background: var(--gold); margin-bottom: 6px; }
  .wordmark-name { font-size: 16px; line-height: 1; letter-spacing: 0.5px; }
  .wordmark-sub { font-size: 6px; letter-spacing: 1.6px; margin-top: 2px; }
  .team-page .wordmark { left: 212px; top: 578px; width: 130px; }

  /* Cover */
  .cover-page { background: var(--paper); }
  .cover-field {
    position: absolute; left: 0; width: 540px;
    background: linear-gradient(125deg, var(--gold) 0%, var(--gold-soft) 30%, var(--gold) 55%, var(--gold-soft) 80%, var(--gold-deep) 100%);
  }
  .cover-field.top { top: 0; height: 342px; }
  .cover-field.bottom { top: 404px; height: 330px; }
  .cover-title {
    position: absolute; left: 22px; top: 357px;
    font-size: 26px; line-height: 1; color: var(--ink); white-space: nowrap;
  }
  .cover-title strong { font-weight: 900; letter-spacing: 0.2px; }
  .cover-title span { font-weight: 300; letter-spacing: -0.3px; }
  .cover-page .wordmark { left: 22px; top: 588px; width: 110px; }
  .cover-page .wordmark-square { background: var(--ink); }
</style>
</head>
<body>
<main class="spread">
  <section class="page team-page">
    <aside class="team-sidebar">
      <h2 class="team-heading">OUR TEAM</h2>
      <div class="member-card">
        <div class="member-photo" role="img" aria-label="Portrait photo of Martin Calder"></div>
        <div class="member-name">MARTIN CALDER,</div>
        <div class="member-title">CFA, CPA,<br>FOUNDER</div>
      </div>
      <div class="member-card">
        <div class="member-photo" role="img" aria-label="Portrait photo of Devin Ashford"></div>
        <div class="member-name">DEVIN ASHFORD,</div>
        <div class="member-title">CFA,<br>FOUNDER</div>
      </div>
      <div class="member-card">
        <div class="member-photo" role="img" aria-label="Portrait photo of Owen Ashford"></div>
        <div class="member-name">OWEN ASHFORD</div>
        <div class="member-title">FOUNDER</div>
      </div>
    </aside>

    <article class="bio first">
      <p>Martin works collaboratively with advisors to formulate successful transition plans. He brings creative insight and deep experience to this niche industry that is sorely lacking in both. Prior to his current role, Martin worked at Meridian Fund Partners where he rose quickly to Regional Director and developed relationships with advisors throughout the Western US. He loved his role at the firm, but became frustrated when some of his closest clients struggled to find the right partner for succession. He witnessed deals implode due to cultural, philosophical, and operational differences and in some cases firms gave up their succession search altogether. He founded Harbrook Counsel Group to make sure advisors find the succession partner they deserve.</p>
      <p>Martin earned a bachelor's degree in Finance from Northfield University. He is a Certified Public Accountant and a CFA Charterholder. Martin enjoys spending time with his wife Helena, traveling internationally, studying foreign languages, and staying active.</p>
    </article>
    <hr class="bio-rule first">
    <article class="bio second">
      <p>Devin has over ten years of experience in the financial services industry. Prior to joining Harbrook Counsel Group, he has served as Portfolio Manager and research analyst for various financial service companies, both large and small. Devin wears multiple hats for the organization: he leads the portfolio management team, oversees our operations staff and handles the technological integration between firms. He has been involved in multiple Advisor mergers and transitions and understands the challenges that firms face when looking for a succession partner. Devin grew up in Southern California and earned a BA from Ridgemont College where he studied Public Policy, Economics and German. He holds the Chartered Financial Analyst (CFA) designation.</p>
      <p>Devin enjoys spending his coveted free time with his wife Marissa and 4 young children. Devin's hobbies include martial arts, reading, cooking, and taking interesting MOOC courses.</p>
    </article>
    <hr class="bio-rule second">
    <article class="bio third">
      <p>Owen brings over 10 years of M&amp;A experience to Harbrook Counsel Group. His expertise in deal structure, operational management, and corporate finance allow him to design customized succession plans for advisors. Owen is previously experienced in commercial finance, in 1998 he co-founded Keystone Capital Funding; and serving as President and Managing Member, built a 100+ employee &amp; $35mm revenue equipment leasing company, which he sold in July 2008. Owen attended Westbay University and earned a Bachelor of Arts degree in English Literature while obtaining a minor in Economics and Communications.</p>
      <p>Owen and his wife Celia have 4 active young children. Owen's hobbies include competing in triathlons throughout the United States, traveling, gourmet cooking, and spending time with family.</p>
    </article>

    <div class="wordmark">
      <div class="wordmark-square"></div>
      <div class="wordmark-name">HARBROOK</div>
      <div class="wordmark-sub">COUNSEL GROUP</div>
    </div>
  </section>

  <section class="page cover-page">
    <div class="cover-field top" role="img" aria-label="Decorative pattern of flowing gold and white curved bands"></div>
    <h1 class="cover-title"><strong>REDEFINING</strong> <span>INVESTMENT ADVICE</span></h1>
    <div class="cover-field bottom" role="img" aria-label="Decorative pattern of flowing gold and white curved bands"></div>
    <div class="wordmark">
      <div class="wordmark-square"></div>
      <div class="wordmark-name">HARBROOK</div>
      <div class="wordmark-sub">COUNSEL GROUP</div>
    </div>
  </section>
</main>
</body>
</html>
```